I need the Scorecard I've developed for my staff to be produced into a visually engaging piece that will encourage the staff to utilize it on a daily basis. I'm thinking it could be 5x7 in size so that it isn't too cumbersome, but I'm open to different layouts.
I have multiple other departments that will need Scorecards created for them as well, but each one will contain task specific questions for each department.

```html
<!DOCTYPE html>
<html lang="en">
<head>
<meta charset="utf-8">
<title>Receptionist Daily Excellence Scorecard</title>
<link rel="stylesheet" href="https://fonts.googleapis.com/css2?family=Poppins:wght@400;500;600;700&family=Open+Sans:ital,wght@0,400;0,600;1,400&display=swap">
<style>
:root{
  --navy:#0c2450;
  --navy-deep:#081a3c;
  --lime:#4fdc1f;
  --ink:#1a1a1a;
  --muted:#555;
  --row-line:#d3d3d3;
  --row-alt:#f2f2f2;
  --sec-call:#e53935;
  --sec-busy:#b3161b;
  --sec-sched:#0e3a8a;
  --sec-cloth:#1e7a12;
  --sec-dc:#b8862b;
  --sec-route:#2b7de1;
  --dot-green:#2bb32b;
  --dot-amber:#e6a317;
  --dot-red:#e02020;
  --card:#ffffff;
}
*{box-sizing:border-box;margin:0;padding:0}
html,body{width:1200px;height:797px;overflow:hidden;background:#fff}
body{position:relative;font-family:"Poppins",sans-serif;color:var(--ink)}
.page{position:absolute;top:24px;width:534px;height:749px;background:#fff;box-shadow:0 3px 14px rgba(0,0,0,.18);overflow:hidden}
.page--front{left:42px}
.page--back{left:623px}
.header-band{position:absolute;left:0;top:0;width:534px;height:114px}
.title{position:absolute;left:0;right:0;top:16px;text-align:center;color:#fff;font-weight:600;font-size:20.5px;letter-spacing:.2px}
.title em{font-style:normal;color:var(--lime)}
.info-pill{position:absolute;left:60px;top:51px;width:414px;height:26px;background:#fff;border-radius:9px;display:flex;align-items:center;padding:0 13px;gap:12px;font-family:"Open Sans",sans-serif;font-size:8px;color:#444}
.info-pill span{flex:1;display:flex;align-items:baseline;gap:3px}
.info-pill i{flex:1;border-bottom:.6px solid #bbb;height:6px}
.rating-note{position:absolute;left:0;right:0;top:84px;text-align:center;color:#fff;font-family:"Open Sans",sans-serif;font-style:italic;font-size:8px}
.photo-fade{position:absolute;left:0;top:430px;width:534px;height:319px;background:linear-gradient(180deg,rgba(230,232,238,0) 0%,rgba(225,228,235,.7) 45%,rgba(215,218,226,.8) 100%)}
.section{position:absolute;left:48px;width:438px}
.page--back .section{left:49px}
.badge{position:relative;height:18px;display:inline-flex;align-items:center;padding:0 7px 0 24px;border-radius:9px;color:#fff;font-weight:600;font-size:8.6px;margin-left:2px}
.badge .icon{position:absolute;left:-3px;top:-2px;width:22px;height:22px;border-radius:50%;background:#fff;border:1.5px solid currentColor;display:flex;align-items:center;justify-content:center}
.badge .icon svg{width:12px;height:12px}
.sec-call .badge{background:var(--sec-call)} .sec-call .icon{color:var(--sec-call)}
.sec-busy .badge{background:var(--sec-busy)} .sec-busy .icon{color:var(--sec-busy)}
.sec-sched .badge{background:var(--sec-sched)} .sec-sched .icon{color:var(--sec-sched)}
.sec-cloth .badge{background:var(--sec-cloth)} .sec-cloth .icon{color:var(--sec-cloth)}
.sec-dc .badge{background:var(--sec-dc)} .sec-dc .icon{color:var(--sec-dc)}
.sec-route .badge{background:var(--sec-route)} .sec-route .icon{color:var(--sec-route)}
.task-head{display:grid;grid-template-columns:180px 104px 1fr;height:16px;margin-top:6px;font-size:7px;align-items:end}
.task-head div{padding:0 6px 2px;height:100%;display:flex;align-items:flex-end}
.task-head .rate{border-left:.8px solid var(--row-line);border-right:.8px solid var(--row-line);justify-content:center;font-weight:600}
.task-head .rate small{font-size:5.5px;font-weight:500;margin-left:2px}
.task-head .notes{font-family:"Open Sans",sans-serif;color:#444;font-size:7px}
.task-head .label{font-weight:500}
.sec-sched .task-head .label,.sec-route .task-head .label{color:var(--sec-sched)}
.task-row{display:grid;grid-template-columns:180px 104px 1fr;height:21.5px;margin-bottom:3.9px;border:.8px solid var(--row-line);border-radius:5px;background:#fff;font-size:8px;font-weight:500}
.task-row:nth-of-type(even){background:var(--row-alt)}
.task-row div{display:flex;align-items:center;padding:0 6px}
.task-row div+div{border-left:.8px solid var(--row-line)}
.status{position:absolute;left:49px;top:318px}
.status h2,.reflection h2{font-size:11px;font-weight:600}
.status ul{list-style:none;margin-top:5px;font-family:"Open Sans",sans-serif;font-size:8px;color:#333}
.status li{display:flex;align-items:center;gap:6px;height:12.3px}
.status li::before{content:"";width:7px;height:7px;border-radius:50%;background:var(--c)}
.reflection{position:absolute;left:49px;top:400px;width:434px}
.reflection h2{display:flex;align-items:center;gap:5px}
.reflection .q{font-family:"Open Sans",sans-serif;font-size:8.4px;color:#333;display:flex;align-items:flex-end;gap:3px;height:14px}
.reflection .q i{flex:1;border-bottom:.6px solid #bbb;margin-bottom:2px}
.reflection .line{border-bottom:.6px solid #bbb;height:10px;margin-bottom:16px}
.footer-band{position:absolute;left:0;top:536px;width:534px;height:213px}
.supervisor-card{position:absolute;left:38px;top:569px;width:459px;height:190px;background:var(--card);border-radius:11px;padding:10px 16px 0 11px}
.supervisor-card h3{font-size:9.6px;font-weight:700;color:var(--ink);margin-left:5px}
.supervisor-card h3 span{color:var(--sec-sched)}
.note-box{height:29px;border:.8px solid var(--row-line);border-radius:6px;margin-top:6px;padding:4px 7px;font-size:8px;font-weight:600;display:flex;gap:4px}
.note-box svg{width:8px;height:8px;flex:none;margin-top:2px}
.manager{display:flex;align-items:center;margin-top:7px;gap:7px}
.manager .label{color:var(--sec-sched);font-weight:700;font-size:9.6px;line-height:1.1}
.manager .label small{display:block;font-size:4.5px;font-weight:400;font-family:"Open Sans",sans-serif}
.manager .box{flex:1;height:26px;border:.8px solid var(--row-line);border-radius:6px}
.signatures{display:flex;gap:14px;margin-top:13px;font-family:"Open Sans",sans-serif;font-size:7.4px;color:#444}
.signatures span{display:flex;gap:3px;flex:1;align-items:flex-end}
.signatures span:last-child{flex:.55}
.signatures i{flex:1;border-bottom:.6px solid #bbb;margin-bottom:2px}
</style>
</head>
<body>

<section class="page page--front">
  <div class="photo-fade" role="img" aria-label="Faded background photo of receptionists wearing headsets"></div>
  <svg class="header-band" viewBox="0 0 534 114" preserveAspectRatio="none"><path d="M0 0H534V93Q267 135 0 93Z" fill="var(--navy)"/></svg>
  <h1 class="title">Receptionist Daily <em>Excellence Scorecard</em></h1>
  <div class="info-pill">
    <span>Name: <i></i></span><span>Date: <i></i></span><span>Location: <i></i></span>
  </div>
  <p class="rating-note">(Please rate yourself for each task: 1 = Needs Improvement, 3 = Meets Expectations, 5 = Excellent)</p>

  <div class="section sec-call" style="top:126px">
    <div class="badge"><span class="icon"><svg viewBox="0 0 12 12"><circle cx="6" cy="4" r="2.4" fill="currentColor"/><path d="M1.5 11.5a4.5 4.5 0 0 1 9 0Z" fill="currentColor"/></svg></span>1.Call Handling &amp; First Call Intake</div>
    <div class="task-head"><div class="label">Task:</div><div class="rate">Self-Rating<small>(1-5)</small></div><div class="notes">Notes / Issues:</div></div>
    <div class="task-row"><div>Answered 90%+ calls within 3 rings</div><div></div><div></div></div>
    <div class="task-row"><div>Maintained empathy and professionalism</div><div></div><div></div></div>
    <div class="task-row"><div>Accurately completed all First Call fields</div><div></div><div></div></div>
    <div class="task-row"><div>Worked within Receptionist role</div><div></div><div></div></div>
  </div>

  <div class="section sec-busy" style="top:284px">
    <div class="badge"><span class="icon"><svg viewBox="0 0 12 12"><path d="M3 1.5l1.8 2.3-1 1.2a6 6 0 0 0 3.2 3.2l1.2-1 2.3 1.8-1 1.8C5.5 10.5 1.5 6.5 1.2 2.5Z" fill="currentColor"/></svg></span>2.Call Management During Busy Times</div>
    <div class="task-head"><div class="label">Task:</div><div class="rate">Self-Rating<small>(1-5)</small></div><div class="notes">Notes / Issues:</div></div>
    <div class="task-row"><div>Prioritized urgent vs. non-urgent calls</div><div></div><div></div></div>
    <div class="task-row"><div>Hold times under 1 minute</div><div></div><div></div></div>
    <div class="task-row"><div>Logged all calls</div><div></div><div></div></div>
    <div class="task-row"><div>Requested help if overwhelmed</div><div></div><div></div></div>
  </div>

  <div class="section sec-sched" style="top:441px">
    <div class="badge"><span class="icon"><svg viewBox="0 0 12 12"><rect x="1" y="2" width="10" height="9" rx="1" fill="none" stroke="currentColor" stroke-width="1.2"/><path d="M1 4.5h10M3.5 6.5h1M6 6.5h1M8.5 6.5h1M3.5 8.5h1M6 8.5h1" stroke="currentColor" stroke-width="1.2"/></svg></span>3.Scheduling Accuracy</div>
    <div class="task-head"><div class="label">Task:</div><div class="rate">Self-Rating<small>(1-5)</small></div><div class="notes">Notes / Issues:</div></div>
    <div class="task-row"><div>Updated scheduling board</div><div></div><div></div></div>
    <div class="task-row"><div>Cross-checked with Red Book</div><div></div><div></div></div>
    <div class="task-row"><div>Entered manifold info promptly</div><div></div><div></div></div>
  </div>

  <div class="section sec-cloth" style="top:569px">
    <div class="badge"><span class="icon"><svg viewBox="0 0 12 12"><path d="M6 11C3 9 2 6 3 2c2 1 3 3 3 6 0-3 1-5 3-6 1 4 0 7-3 9Z" fill="currentColor"/></svg></span>4.Clothing &amp; Flowers</div>
    <div class="task-head"><div class="label">Task:</div><div class="rate">Self-Rating<small>(1-5)</small></div><div class="notes">Notes / Issues:</div></div>
    <div class="task-row"><div>Clothing sheet completed</div><div></div><div></div></div>
    <div class="task-row"><div>Family contact noted on sheet</div><div></div><div></div></div>
    <div class="task-row"><div>Floral deliveries logged</div><div></div><div></div></div>
    <div class="task-row"><div>Concerns communicated to Care Center</div><div></div><div></div></div>
    <div class="task-row"><div>Flower placement verified</div><div></div><div></div></div>
  </div>
</section>

<section class="page page--back">
  <div class="section sec-dc" style="top:24px">
    <div class="badge"><span class="icon"><svg viewBox="0 0 12 12"><rect x="2.5" y="1" width="7" height="10" rx="1" fill="currentColor"/><path d="M4 4h4M4 6h4M4 8h2.5" stroke="#fff" stroke-width="1"/></svg></span>5.Death Certificates</div>
    <div class="task-head"><div class="label">Task:</div><div class="rate">Self-Rating<small>(1-5)</small></div><div class="notes">Notes / Issues:</div></div>
    <div class="task-row"><div>Verified recipient ID &amp; relationship</div><div></div><div></div></div>
    <div class="task-row"><div>Confirmed correct documents enclosed</div><div></div><div></div></div>
    <div class="task-row"><div>Recipient signed the DC logbook</div><div></div><div></div></div>
    <div class="task-row"><div>Suggested proofreading before leaving</div><div></div><div></div></div>
  </div>

  <div class="section sec-route" style="top:181px">
    <div class="badge"><span class="icon"><svg viewBox="0 0 12 12"><path d="M1 2h7v5H4l-2 2V7H1Z" fill="currentColor"/><path d="M9 4h2v5h-1v1.5L8.5 9H5V8h4Z" fill="currentColor"/></svg></span>6.Routing &amp; Messages</div>
    <div class="task-head"><div class="label">Task:</div><div class="rate">Self-Rating<small>(1-5)</small></div><div class="notes">Notes / Issues:</div></div>
    <div class="task-row"><div>Calls routed appropriately</div><div></div><div></div></div>
    <div class="task-row"><div>Messages included all required info</div><div></div><div></div></div>
    <div class="task-row"><div>Delivered 95%+ messages in 30 min</div><div></div><div></div></div>
  </div>

  <div class="status">
    <h2>Daily Status Summary (Circle One)</h2>
    <ul>
      <li style="--c:var(--dot-green)">Excellent – All key duties completed, proactive, calm under pressure</li>
      <li style="--c:var(--dot-amber)">Satisfactory – Most duties completed, minor follow-up needed</li>
      <li style="--c:var(--dot-red)">Needs Support – Missed urgent duties, accuracy or stress issues</li>
    </ul>
  </div>

  <div class="reflection">
    <h2><svg width="11" height="11" viewBox="0 0 12 12"><rect x="1" y="2" width="8" height="9" rx="1" fill="#f3e6b8" stroke="#b8862b" stroke-width=".8"/><path d="M5 8l5-6 1 1-5 6-1.5.5Z" fill="#e0a100"/></svg>Daily Reflection</h2>
    <div style="height:10px"></div>
    <div class="q">What went well today? <i></i></div>
    <div class="line"></div>
    <div class="q">Any issues or barriers to note? <i></i></div>
    <div class="line"></div>
    <div class="q">Support needed from supervisor? <i></i></div>
    <div class="line"></div>
  </div>

  <svg class="footer-band" viewBox="0 0 534 213" preserveAspectRatio="none"><path d="M0 0Q267 26 534 0V213H0Z" fill="var(--navy-deep)"/></svg>

  <div class="supervisor-card">
    <h3>Stars &amp; Flags (<span>Supervisor Use Only</span>)</h3>
    <div class="note-box"><svg viewBox="0 0 10 10"><path d="M5 0l1.3 3.7L10 5 6.3 6.3 5 10 3.7 6.3 0 5l3.7-1.3Z" fill="#f2c200"/></svg>Stars (Excellence or above-and-beyond moments):</div>
    <div class="note-box"><svg viewBox="0 0 10 10"><path d="M1.5 0v10" stroke="#555" stroke-width="1"/><path d="M2 .5h7L7.5 3 9 5.5H2Z" fill="#e02020"/></svg>Flags (Concerns needing follow-up/coaching):</div>
    <div class="manager">
      <div class="label">Manager Overall Rating (1-5):<small>(Manager: Please rate overall performance on a 1-5 scale)</small></div>
      <div class="box"></div>
    </div>
    <div class="signatures">
      <span>Receptionist Signature: <i></i></span>
      <span>Supervisor Signature: <i></i></span>
      <span>Date: <i></i></span>
    </div>
  </div>
</section>

</body>
</html>
```